Velmorytrips.com web design project + logo design

Hi,

We are a Russian online tour operator - roamquiltex.com

We are looking to tranmsfer our domain to velmorytrips.com. The website and logo need to be velmoryesque - we are not looking to change our functionality, but we need to make the website much more attracitve to clients, much more wild looking but at the same time remaining a professional travel company.

The main concept of the website should be innovative travel (as velmory was an innovator). Alternatively, you could go down the artist route and go down the draw / design your own tour road.

On our website the customer is able to combine travel services (hotels, flights, Visa services, and soon chauffeur, car rental etc...) put it into their basket (the basket definitely has to look better than it is at the moment) and pay for it in one go by card.

We are also stressin our customer support with web chat, call centre etc... (call centre number at the top of the page)

We aim to provide an easy user experience, but we need to make it have some more style, so I will be waiting for what you guys can come up with.
Let me know if you have any questions - skype is: mrkostelin

Industry/Entity Type

It Company

Logo Text

Requirements
Must have
• It is quite a simple task - to take the existing website roamquiltex.com and velmorysize it to create velmorytrips.com, the functionality of the website will remain the same and there are not many pages in the website. Homepage, Checkout step1, Checkout step 2 (you can view both of these if you select a service) and the generic pages for T&C''s, Privacy policy etc...

IMPORTANT UPDATE

We are also looking at how the search results will look in the designs, (please do a search on our website for hotel / flight)

```html
<!DOCTYPE html>
<html lang="ru">
<head>
<meta charset="utf-8">
<title>Velmorytrips.com — Больше чем опыт путешествия</title>
<link rel="stylesheet" href="https://fonts.googleapis.com/css2?family=Open+Sans:wght@300;400;600;700&display=swap">
<style>
  :root {
    --header-bg: #2e2e2e;
    --brand-blue: #5aa9cc;
    --panel-blue: rgba(44, 78, 102, 0.88);
    --panel-dark: rgba(38, 58, 68, 0.9);
    --panel-black: #0b0b0b;
    --field-bg: #5f5f5f;
    --field-text: #d6d6d6;
    --label: #444;
    --tab-active: #d9d9d9;
    --search-btn: #4690bb;
    --footer-bg: #3c4a52;
    --footer-black: #0d0d0d;
    --footer-cell: #2c2c2c;
    --footer-cell-mid: #3a4850;
    --white: #ffffff;
  }
  * { box-sizing: border-box; margin: 0; padding: 0; }
  html, body { width: 1029px; height: 1200px; overflow: hidden; }
  body { position: relative; background: var(--white); font-family: "Open Sans", Arial, sans-serif; color: var(--label); }

  .site-header { position: absolute; left: 0; top: 0; width: 1029px; height: 94px; background: var(--header-bg); }
  .brand { position: absolute; display: flex; align-items: center; gap: 10px; color: var(--brand-blue); font-weight: 300; letter-spacing: 0.5px; }
  .brand-mark { width: 44px; height: 44px; border-radius: 50%; border: 3px solid var(--brand-blue); }
  .site-header .brand { left: 92px; top: 24px; font-size: 29px; }
  .top-nav { position: absolute; top: 40px; left: 463px; display: flex; align-items: center; font-size: 11px; color: #e6e6e6; text-transform: uppercase; }
  .top-nav .nav-item { display: flex; align-items: center; gap: 6px; }
  .nav-forum { margin-right: 62px; }
  .nav-lang { margin-right: 56px; }
  .nav-tour { margin-right: 26px; }
  .cart-button { background: #d6d6d6; color: #222; font-size: 9px; padding: 5px 8px; display: flex; align-items: center; gap: 4px; margin-left: 4px; }

  .hero { position: absolute; left: 0; top: 94px; width: 1029px; height: 506px;
    background: linear-gradient(180deg, #5c84a6 0%, #9ab0bf 14%, #b49a5c 32%, #7a6a3c 48%, #2d3424 68%, #1a1d16 100%); }
  .contact-phones { position: absolute; left: 86px; top: 382px; width: 321px; height: 114px; background: var(--panel-blue); color: var(--white); }
  .phone-main { position: absolute; left: 26px; top: 28px; font-size: 29px; font-weight: 700; }
  .phone-alt { position: absolute; right: 14px; top: 62px; font-size: 20px; font-weight: 300; }
  .working-hours { position: absolute; left: 86px; top: 496px; width: 321px; height: 104px; background: var(--panel-black); color: var(--white); }
  .hours-days { position: absolute; left: 32px; top: 16px; font-size: 18px; }
  .hours-time { position: absolute; left: 62px; top: 38px; font-size: 30px; }
  .hours-pointer { position: absolute; left: 362px; top: 600px; }
  .tagline { position: absolute; left: 407px; top: 382px; width: 509px; height: 218px; background: var(--panel-dark); color: var(--white); text-align: center; }
  .tagline-big { display: block; font-size: 90px; line-height: 1; margin-top: 12px; }
  .tagline-mid { display: block; font-size: 34px; line-height: 1; margin-top: 2px; }
  .tagline-low { display: block; font-size: 60px; line-height: 1; margin-top: -2px; }

  .checkout-steps { position: absolute; left: 99px; top: 629px; display: flex; font-size: 18px; color: #2b3a42; }
  .step { height: 33px; line-height: 33px; padding: 0 13px; }
  .step.active { background: var(--tab-active); }
  .step-empty { margin-left: 16px; line-height: 26px; }
  .step-pay { margin-left: 6px; }
  .divider { position: absolute; left: 0; width: 1029px; height: 6px;
    background: radial-gradient(ellipse at center top, rgba(0,0,0,0.18), rgba(0,0,0,0) 70%); }

  .search-form { position: absolute; left: 0; top: 680px; width: 1029px; height: 230px; }
  .label { position: absolute; font-size: 14px; color: var(--label); }
  .field { position: absolute; height: 33px; background: var(--field-bg); color: var(--field-text); font-size: 11px; line-height: 33px; padding-left: 11px; display: flex; align-items: center; }
  .select-arrow { position: absolute; right: 0; top: 0; width: 29px; height: 33px; background: #c9c9c9; display: flex; align-items: center; justify-content: center; }
  .help { position: absolute; width: 16px; height: 16px; border-radius: 50%; background: #c6c6c6; color: #fff; font-size: 11px; font-weight: 700; text-align: center; line-height: 16px; }
  .trip-type { position: absolute; left: 601px; top: 112px; font-size: 10px; color: #333; line-height: 17px; }
  .trip-type span { display: flex; align-items: center; gap: 5px; }
  .box { width: 10px; height: 10px; border: 1px solid #777; background: #d9d9d9; display: inline-block; }
  .box.checked { background: #555; box-shadow: inset 0 0 0 2px #d9d9d9; }
  .search-button { position: absolute; left: 597px; top: 168px; width: 242px; height: 33px; background: var(--search-btn); color: #fff; font-size: 15px; display: flex; align-items: center; justify-content: center; gap: 6px; }

  .site-footer { position: absolute; left: 0; top: 1010px; width: 1029px; height: 190px; background: var(--footer-bg); color: #fff; }
  .footer-col { position: absolute; top: 32px; font-size: 11px; line-height: 14.5px; }
  .footer-col h3 { font-size: 14px; font-weight: 400; margin-bottom: 16px; }
  .footer-contact { position: absolute; left: 455px; top: 0; width: 476px; height: 190px; background: var(--footer-black); }
  .footer-contact .brand { right: 11px; top: 16px; font-size: 22px; gap: 8px; }
  .footer-contact .brand-mark { width: 34px; height: 34px; border-width: 2px; }
  .socials { position: absolute; right: 15px; top: 56px; display: flex; gap: 8px; }
  .socials span { width: 31px; height: 31px; border-radius: 50%; background: #fff; }
  .contact-cell { position: absolute; top: 134px; height: 56px; width: 159px; font-size: 12px; line-height: 15px; display: flex; align-items: center; justify-content: center; text-align: left; }
  .contact-icon { position: absolute; top: -20px; left: 50%; margin-left: -17px; }
</style>
</head>
<body>

<header class="site-header">
  <div class="brand"><span class="brand-mark"></span>VELMORYTRAVEL</div>
  <nav class="top-nav">
    <span class="nav-item nav-forum">
      <svg width="18" height="16" viewBox="0 0 18 16"><rect x="1" y="3" width="12" height="12" fill="none" stroke="#ddd" stroke-width="1.5"/><path d="M7 10 L15 2 L17 4 L9 12 L6 13 Z" fill="#ddd"/></svg>Форум</span>
    <span class="nav-item nav-lang">
      <svg width="18" height="12" viewBox="0 0 18 12"><rect width="18" height="4" fill="#fff"/><rect y="4" width="18" height="4" fill="#bbb"/><rect y="8" width="18" height="4" fill="#888"/></svg>Язык</span>
    <span class="nav-item nav-tour">
      <svg width="18" height="16" viewBox="0 0 18 16"><path d="M1 3 L6 1 L12 3 L17 1 L17 13 L12 15 L6 13 L1 15 Z" fill="#ccc"/></svg>Мой тур</span>
    <span class="nav-item">
      <svg width="22" height="20" viewBox="0 0 22 20"><path d="M1 2 H5 L8 13 H18 L20 5 H6" fill="none" stroke="#ddd" stroke-width="1.6"/><circle cx="9" cy="17" r="1.6" fill="#ddd"/><circle cx="17" cy="17" r="1.6" fill="#ddd"/></svg>
      <span class="cart-button">Корзина (0)
        <svg width="8" height="5" viewBox="0 0 8 5"><path d="M0 0 H8 L4 5 Z" fill="#222"/></svg></span>
    </span>
  </nav>
</header>

<section class="hero" role="img" aria-label="Фотография: залитые закатным солнцем альпийские горы со снежными вершинами и лесистой долиной"></section>

<div class="contact-phones">
  <span class="phone-main">8-800-555-0142</span>
  <span class="phone-alt">+7 (495) 555-01-37</span>
</div>
<div class="working-hours">
  <span class="hours-days">(Пн-Пт) Часы работы</span>
  <span class="hours-time">с 9:00 - до 18:00</span>
</div>
<svg class="hours-pointer" width="28" height="14" viewBox="0 0 28 14"><path d="M0 0 H28 L14 14 Z" fill="#0b0b0b"/></svg>
<div class="tagline">
  <span class="tagline-big">Больше</span>
  <span class="tagline-mid">чем опыт</span>
  <span class="tagline-low">путешествия</span>
</div>

<nav class="checkout-steps">
  <span class="step active">Корзина</span>
  <span class="step step-empty">пусто</span>
  <span class="step step-pay">Оплата</span>
</nav>
<div class="divider" style="top:662px"></div>

<form class="search-form">
  <span class="label" style="left:112px;top:21px">Откуда</span>
  <span class="field" style="left:216px;top:13px;width:279px">Город</span>
  <span class="label" style="left:539px;top:21px">Куда</span>
  <span class="field" style="left:600px;top:13px;width:239px">Город</span>

  <span class="label" style="left:112px;top:73px">Туда</span>
  <span class="field" style="left:216px;top:62px;width:281px;padding-left:4px">
    <svg width="24" height="24" viewBox="0 0 24 24" style="margin-right:10px"><rect x="1" y="3" width="22" height="20" fill="#ddd"/><rect x="1" y="3" width="22" height="5" fill="#aaa"/><text x="12" y="21" font-size="12" font-weight="700" text-anchor="middle" fill="#555" font-family="Open Sans, sans-serif">7</text></svg>(16-6-2013)</span>
  <span class="label" style="left:536px;top:79px">Обратно</span>
  <span class="field" style="left:600px;top:67px;width:239px;padding-left:8px">(Обратно)</span>

  <span class="label" style="left:112px;top:125px">Пассажиры</span>
  <span class="field" style="left:216px;top:113px;width:75px;padding-left:5px">
    <svg width="10" height="20" viewBox="0 0 10 20"><circle cx="5" cy="3" r="2.6" fill="#ccc"/><rect x="2" y="7" width="6" height="13" fill="#ccc"/></svg>&nbsp;&nbsp;(1)
    <span class="select-arrow"><svg width="10" height="6" viewBox="0 0 10 6"><path d="M0 0 H10 L5 6 Z" fill="#333"/></svg></span></span>
  <span class="help" style="left:297px;top:118px">?</span>
  <span class="field" style="left:318px;top:113px;width:75px;padding-left:5px">
    <svg width="10" height="20" viewBox="0 0 10 20"><circle cx="5" cy="3" r="2.6" fill="#ccc"/><rect x="2" y="7" width="6" height="13" fill="#ccc"/></svg>&nbsp;&nbsp;(0)
    <span class="select-arrow"><svg width="10" height="6" viewBox="0 0 10 6"><path d="M0 0 H10 L5 6 Z" fill="#333"/></svg></span></span>
  <span class="help" style="left:399px;top:118px">?</span>
  <span class="field" style="left:420px;top:113px;width:75px;padding-left:3px">
    <svg width="14" height="20" viewBox="0 0 14 20"><circle cx="7" cy="4" r="3" fill="#ccc"/><rect x="3" y="9" width="8" height="7" fill="#ccc"/><circle cx="4" cy="18" r="2" fill="#ccc"/><circle cx="10" cy="18" r="2" fill="#ccc"/></svg>&nbsp;&nbsp;(0)
    <span class="select-arrow"><svg width="10" height="6" viewBox="0 0 10 6"><path d="M0 0 H10 L5 6 Z" fill="#333"/></svg></span></span>
  <span class="help" style="left:500px;top:118px">?</span>

  <div class="trip-type">
    <span><i class="box"></i>Обратно</span>
    <span><i class="box checked"></i>В одну сторону</span>
  </div>

  <span class="label" style="left:112px;top:177px">Класс</span>
  <span class="field" style="left:215px;top:168px;width:282px">Эконом
    <span class="select-arrow"><svg width="10" height="6" viewBox="0 0 10 6"><path d="M0 0 H10 L5 6 Z" fill="#333"/></svg></span></span>

  <span class="search-button">
    <svg width="17" height="17" viewBox="0 0 17 17"><circle cx="7" cy="7" r="5" fill="none" stroke="#fff" stroke-width="2.4"/><path d="M11 11 L16 16" stroke="#fff" stroke-width="2.8"/></svg>Поиск</span>
</form>
<div class="divider" style="top:934px"></div>

<footer class="site-footer">
  <div class="footer-col" style="left:113px">
    <h3>Просмотр Сайта</h3>
    Домой<br>О нас<br>Форум<br>Контакты<br>Помощь
  </div>
  <div class="footer-col" style="left:308px">
    <h3>Помощь</h3>
    Помощь<br>Правила<br>пользования<br>Политика<br>конфиденциал<br>ьности<br>Cookies
  </div>
  <div class="footer-contact">
    <div class="brand"><span class="brand-mark"></span>VELMORYTRAVEL</div>
    <div class="socials" aria-label="Социальные сети"><span></span><span></span><span></span></div>

    <div class="contact-cell" style="left:0;background:var(--footer-cell)">
      <svg class="contact-icon" width="34" height="34" viewBox="0 0 34 34"><circle cx="17" cy="17" r="15" fill="#0d0d0d" stroke="#fff" stroke-width="2"/><path d="M17 26 C12 19 11 16 11 14 A6 6 0 0 1 23 14 C23 16 22 19 17 26 Z" fill="none" stroke="#fff" stroke-width="1.8"/><circle cx="17" cy="14" r="2" fill="#fff"/></svg>
      <span>14 Larkfield Row<br>London, E2 7QX,UK</span>
    </div>
    <div class="contact-cell" style="left:159px;background:var(--footer-cell-mid)">
      <svg class="contact-icon" width="34" height="34" viewBox="0 0 34 34"><circle cx="17" cy="17" r="15" fill="#0d0d0d" stroke="#fff" stroke-width="2"/><rect x="12" y="9" width="10" height="16" rx="1.5" fill="none" stroke="#fff" stroke-width="1.8"/><rect x="14" y="11" width="6" height="10" fill="#fff"/></svg>
      <span>+7 (495) 555-01-37</span>
    </div>
    <div class="contact-cell" style="left:317px;background:var(--footer-cell)">
      <svg class="contact-icon" width="34" height="34" viewBox="0 0 34 34"><circle cx="17" cy="17" r="15" fill="#0d0d0d" stroke="#fff" stroke-width="2"/><rect x="10" y="12" width="14" height="11" fill="none" stroke="#fff" stroke-width="1.8"/><path d="M10 12 L17 18 L24 12" fill="none" stroke="#fff" stroke-width="1.6"/></svg>
      <span>info@roamquiltex.com</span>
    </div>
  </div>
</footer>

</body>
</html>
```